Organic lawn care

take the same sign as the mosquito sign, only instead of the mosquito image have the red circle and line cross out the text of "chemicals". Have the sign say "this lawn receives ORGANIC grass treatments" "instantly SAFE for people and pets"

Lawn Care

```html
<!DOCTYPE html>
<html lang="en">
<head>
<meta charset="utf-8">
<title>Organic Lawn Treatment Sign</title>
<link href="https://fonts.googleapis.com/css2?family=Poppins:wght@300;400;600;800&display=swap" rel="stylesheet">
<style>
  :root {
    --paper: #ffffff;
    --stop-red: #e8262d;
    --stop-yellow: #fff200;
    --ink: #111111;
    --headline-red: #d7262e;
    --organic-green: #8cc63f;
    --safe-blue: #3d9ad6;
  }
  * { margin: 0; padding: 0; box-sizing: border-box; }
  html, body {
    width: 800px;
    height: 1200px;
    overflow: hidden;
    background: var(--paper);
  }
  .sign {
    position: relative;
    width: 800px;
    height: 1200px;
    font-family: "Poppins", "Century Gothic", sans-serif;
    font-weight: 300;
    text-align: center;
  }
  .no-chemicals {
    position: absolute;
    left: 200px;
    top: 64px;
    width: 404px;
    height: 404px;
  }
  .no-chemicals__label {
    font-family: "Poppins", "Arial Black", sans-serif;
    font-weight: 800;
    font-size: 44px;
    fill: var(--ink);
  }
  .line {
    position: absolute;
    left: 0;
    width: 100%;
    line-height: 1;
    white-space: nowrap;
  }
  .headline { color: var(--headline-red); font-size: 58px; }
  .headline--top { top: 512px; }
  .headline--bottom { top: 684px; }
  .organic {
    top: 592px;
    color: var(--organic-green);
    font-size: 92px;
    letter-spacing: 0.2em;
    padding-left: 0.2em;
  }
  .safety { color: var(--safe-blue); font-size: 52px; }
  .safety--top { top: 790px; }
  .safety__word {
    font-size: 84px;
    letter-spacing: 0.14em;
    margin: 0 4px 0 10px;
  }
  .safety--bottom { top: 880px; }
  .contact-site {
    top: 996px;
    color: var(--safe-blue);
    font-size: 58px;
    font-weight: 400;
  }
  .contact-phone {
    top: 1058px;
    color: var(--safe-blue);
    font-size: 48px;
    font-weight: 600;
    letter-spacing: 0.06em;
  }
</style>
</head>
<body>
  <main class="sign">
    <svg class="no-chemicals" viewBox="0 0 404 404" aria-label="No chemicals">
      <circle cx="202" cy="202" r="182" fill="var(--stop-yellow)" stroke="var(--stop-red)" stroke-width="24"/>
      <text class="no-chemicals__label" x="202" y="218" text-anchor="middle">CHEMICALS</text>
      <line x1="73" y1="73" x2="331" y2="331" stroke="var(--stop-red)" stroke-width="24"/>
    </svg>

    <p class="line headline headline--top">this grass receives</p>
    <p class="line organic">ORGANIC</p>
    <p class="line headline headline--bottom">treatments</p>

    <p class="line safety safety--top">instantly<span class="safety__word">SAFE</span>for</p>
    <p class="line safety safety--bottom">people and pets</p>

    <p class="line contact-site">greenmows.com</p>
    <p class="line contact-phone">615-555-0142</p>
  </main>
</body>
</html>
```